new business cards - professional services but interesting please!

I need new business cards using an existing logo and tag line. The colour (yellow) in the current logo needs to be sharpened to be bright yellow (currently it prints with a green-ish tinge).

Business name: Keystone. Talent Partners (please note the dot after Keystone)

My name: Bettina Lorne

Contact detail: phone : +61 (0) 492 315 608
email: bettina@keystone-talentpartners.com.au
web: www.keystone-talentpartners.com.au (note web will provide colour palette for reference)
linkedIn (unsure as to include or not?) https://www.linkedin.com/in/bettinaroselorne/

Tag line: lifting workplace momentum (seems to sit best at bottom of a page with some space away from the logo)

I provide a range of people services (outsourced Human Resources) and I am a leadership coach too. To date I have referred to myself as "Business Coach & Consultant" but think this might be too vague.

Options for card:

1. Bettina Lorne
People & Culture
Consultant & Coach

2. Bettina Lorne
Leadership Coach (front of card) then turn card over:

3. Bettina Lorne
Consultant - People & Culture (back of card)

4. Bettina Lorne
Business Coach & Consultant
Leadership Development I People & Culture I Change Management I Workplace Well-being

I have attached 2 logo copies along with a picture of my current cards. They were printed too small and therefore cant be used. With hindsight, too much content (and a little dull!) Can you help? Happy for ideas too

Thankyou

Target Market(s)

Small business ( Outsourced HR), corporates ( leadership development & coaching)

Industry/Entity Type

Professional Service

Contact Information for Business Card

See above project description

Font styles to use
Sans Serif

Requirements
Must have
• See above project description

```html
<!DOCTYPE html>
<html lang="en">
<head>
<meta charset="UTF-8">
<title>Keystone. Talent Partners — Business Cards</title>
<link rel="stylesheet" href="https://fonts.googleapis.com/css2?family=Roboto:wght@300;400&display=swap">
<style>
  :root {
    --bg: #2e2e2e;
    --slate: #5b666e;
    --silver: #a8acae;
    --yellow: #ffea00;
    --gold: #ffcc00;
    --white: #ffffff;
    --ink-grey: #6e6e6e;
    --logo-grey: #a9adb0;
  }
  * { box-sizing: border-box; margin: 0; padding: 0; }
  html, body { width: 1200px; height: 900px; overflow: hidden; }
  body {
    background: var(--bg);
    font-family: "Roboto", Arial, sans-serif;
    position: relative;
  }
  .card {
    position: absolute;
    top: 300px;
    width: 520px;
    height: 300px;
    overflow: hidden;
    background: var(--white);
  }
  .card--front { left: 65px; }
  .card--back { left: 615px; }

  /* Wordmark: one colour, one weight */
  .wordmark {
    position: absolute;
    display: inline-flex;
    flex-direction: column;
    color: var(--logo-grey);
    font-weight: 300;
    line-height: 1;
    white-space: nowrap;
  }
  .wordmark-name { display: block; }
  .wordmark-sub { display: block; align-self: flex-end; }

  /* Front */
  .front-stripe { position: absolute; left: 0; top: 0; width: 60px; height: 300px; background: var(--yellow); }
  .front-panel { position: absolute; left: 60px; top: 0; right: 0; height: 213px; background: var(--slate); }
  .front-panel .wordmark { left: 72px; top: 70px; }
  .front-panel .wordmark-name { font-size: 64px; letter-spacing: 0.5px; }
  .front-panel .wordmark-sub { font-size: 21px; margin-top: 2px; }
  .front-band {
    position: absolute; left: 60px; top: 213px; right: 0; height: 44px;
    background: var(--gold);
    display: flex; align-items: center; justify-content: center;
    color: var(--ink-grey); font-size: 18px; font-weight: 400; letter-spacing: 0.5px;
  }

  /* Back */
  .back-logo-area { position: absolute; left: 0; top: 0; right: 0; height: 115px; }
  .back-logo-area .wordmark { left: 36px; top: 24px; }
  .back-logo-area .wordmark-name { font-size: 50px; letter-spacing: 0.4px; }
  .back-logo-area .wordmark-sub { font-size: 16px; margin-top: 2px; }
  .name-band {
    position: absolute; left: 0; top: 115px; width: 245px; height: 78px;
    background: var(--yellow); padding: 19px 0 0 36px;
  }
  .person-name { font-size: 20px; font-weight: 400; color: var(--ink-grey); }
  .person-title { font-size: 13px; color: var(--ink-grey); margin-top: 6px; }
  .accent-block { position: absolute; left: 245px; top: 115px; width: 80px; height: 78px; background: var(--gold); }
  .contact-panel { position: absolute; left: 0; top: 193px; right: 0; bottom: 0; background: var(--slate); }
  .services {
    position: absolute; left: 325px; top: 95px; width: 195px; height: 117px;
    background: var(--silver); list-style: none; padding: 24px 0 0 10px;
  }
  .services li {
    color: var(--white); font-size: 13.5px; line-height: 17.5px;
    display: flex; align-items: center; gap: 6px;
  }
  .services li::before {
    content: ""; width: 5px; height: 5px; border-radius: 50%; background: var(--yellow); flex: none;
  }
  .contacts { position: absolute; left: 36px; top: 207px; list-style: none; }
  .contacts li {
    display: flex; align-items: center; gap: 7px;
    color: var(--white); font-size: 13.5px; line-height: 19.5px;
  }
  .contact-icon { width: 14px; height: 14px; flex: none; }
</style>
</head>
<body>
  <section class="card card--front" aria-label="Business card front">
    <div class="front-stripe"></div>
    <div class="front-panel">
      <div class="wordmark">
        <span class="wordmark-name">Keystone.</span>
        <span class="wordmark-sub">Talent Partners</span>
      </div>
    </div>
    <div class="front-band">LIFTING WORKPLACE MOMENTUM</div>
  </section>

  <section class="card card--back" aria-label="Business card back">
    <div class="back-logo-area">
      <div class="wordmark">
        <span class="wordmark-name">Keystone.</span>
        <span class="wordmark-sub">Talent Partners</span>
      </div>
    </div>
    <div class="contact-panel"></div>
    <div class="name-band">
      <p class="person-name">Bettina Lorne</p>
      <p class="person-title">Business Coach &amp; Consultant</p>
    </div>
    <div class="accent-block"></div>
    <ul class="services">
      <li>Leadership Development</li>
      <li>People &amp; Culture</li>
      <li>Change Management</li>
      <li>Workplace Well-being</li>
    </ul>
    <ul class="contacts">
      <li>
        <svg class="contact-icon" viewBox="0 0 14 14" aria-hidden="true"><circle cx="7" cy="7" r="6.2" fill="none" stroke="#ffea00" stroke-width="1.2"/><rect x="4.8" y="3.5" width="4.4" height="7" rx="0.8" fill="none" stroke="#ffea00" stroke-width="1"/></svg>
        +61 (0) 492 315 608
      </li>
      <li>
        <svg class="contact-icon" viewBox="0 0 14 14" aria-hidden="true"><circle cx="7" cy="7" r="7" fill="#ffea00"/><rect x="3.5" y="4.8" width="7" height="4.6" fill="#5b666e"/><path d="M3.5 4.8 L7 7.5 L10.5 4.8" fill="none" stroke="#ffea00" stroke-width="0.9"/></svg>
        bettina@keystone-talentpartners.com.au
      </li>
      <li>
        <svg class="contact-icon" viewBox="0 0 14 14" aria-hidden="true"><circle cx="7" cy="7" r="6.2" fill="none" stroke="#ffea00" stroke-width="1.2"/><ellipse cx="7" cy="7" rx="2.2" ry="4.2" fill="none" stroke="#ffea00" stroke-width="0.9"/><line x1="2.8" y1="7" x2="11.2" y2="7" stroke="#ffea00" stroke-width="0.9"/></svg>
        www.keystone-talentpartners.com.au
      </li>
      <li>
        <svg class="contact-icon" viewBox="0 0 14 14" aria-hidden="true"><circle cx="7" cy="7" r="6.2" fill="none" stroke="#ffea00" stroke-width="1.2"/></svg>
        /bettinaroselorne
      </li>
    </ul>
  </section>
</body>
</html>
```